Design a App to help people have successful dates!

We require an awesome designer to help us with an App design for a new dating app we are introducing! Our App is intended to help Users build confidence is knowing what questions or ask and answer when going on dates! As you can see from our Project Brief, the intent of the app is to display two types of content to the user 1) Dating Questions, and 2) Dating Tips. We have developed wireframes to help convey what each screen should convey. The intent is to 'inform' and 'educate' the User on what questions to ask, or what questions could be asked of them. Also, we would like to include Banner Ads on the 'Question' and 'Tip' screens, which you can see in the brief.

Target Market(s)

Men and women - aged 18 - 45 who need help identifying dating questions

Industry/Entity Type

Dating App

Font styles to use
Sans Serif

Requirements
Must have
• Please review the PDF brief that we have uploaded. Please make the swipe left and right feature modern (I only included the buttons as a guide only). The ‘Romance Prompt Ace’ App is intended to be a light-hearted, simple, elegant, fun App, to help Users ask and engage in dating questions. Think of this app as an 'LoveNest' (high quality, educated Users) to help users with identifying questions to ask on dates.
Nice to have
• Please review the PDF brief that we have uploaded.
Should not have
• The App is intended to only include genuine, legitimate, clean and appropriate content. This is not a 'Flarn' stiyle look-up app.

```html
<!DOCTYPE html>
<html lang="en">
<head>
<meta charset="utf-8">
<title>Romance Prompt Ace – App Screens</title>
<link href="https://fonts.googleapis.com/css2?family=Arvo:wght@400;700&family=Lato:wght@400;700;900&display=swap" rel="stylesheet">
<style>
  :root{
    --stage:#e07c27;
    --ink:#151515;
    --teal:#0e97be;
    --blush:#fcf0f3;
    --blush-deep:#f7e2e8;
    --green:#4caf1e;
    --white:#ffffff;
    --text:#222222;
    --ad:#e07c27;
  }
  *{box-sizing:border-box;margin:0;padding:0}
  html,body{width:847px;height:1200px;overflow:hidden;background:var(--stage)}
  .board{position:relative;width:847px;height:1200px;background:var(--stage)}
  .screen{position:absolute;width:318px;height:542px;overflow:hidden;
    background:radial-gradient(circle at 30% 20%,var(--white) 0,var(--blush) 45%,var(--blush-deep) 100%);
    font-family:'Lato',sans-serif;color:var(--text)}
  .screen--welcome{left:97px;top:41px}
  .screen--menu{left:449px;top:41px}
  .screen--tip{left:97px;top:614px}
  .screen--question{left:449px;top:614px}
  .header-curve{position:absolute;left:0;top:0;width:318px;height:160px}
  .nav-back{position:absolute;left:14px;top:29px;color:var(--white);font-size:11px;font-weight:700;letter-spacing:.3px;display:flex;align-items:center;gap:5px}
  .nav-back svg{width:7px;height:10px}
  .nav-place{position:absolute;left:0;right:0;top:20px;text-align:center;color:var(--white)}
  .nav-place .city{font-size:12.5px;font-weight:700}
  .nav-place .stamp{font-size:9px;margin-top:3px}
  .hero-photo{position:absolute;left:70px;top:28px;width:180px;height:180px;border-radius:50%;
    border:4px solid var(--white);background:linear-gradient(135deg,#8a6a56,#c9a48c 50%,#5b4438)}
  .app-title{position:absolute;left:0;right:0;top:243px;text-align:center;font-family:'Arvo',serif;font-weight:700;
    color:var(--teal);font-size:22px;line-height:27px;letter-spacing:1px}
  .app-subtitle{position:absolute;left:0;right:0;top:301px;text-align:center;font-size:13px;color:var(--text)}
  .pill{position:absolute;left:12px;width:293px;height:42px;border-radius:21px;display:flex;align-items:center;justify-content:center;
    font-family:'Arvo',serif;font-weight:700;font-size:15.5px;letter-spacing:1px;color:var(--white)}
  .pill--dark{top:400px;background:var(--ink)}
  .pill--teal{top:448px;background:var(--teal)}
  .go-icon{position:absolute;width:22px;height:22px}
  .pill .go-icon{right:8px;top:10px}
  .page-count{position:absolute;right:8px;top:521px;font-size:10px;font-weight:700;color:var(--ink);letter-spacing:.5px}
  .avatar{position:absolute;top:131px;width:58px;height:58px;border-radius:50%;border:2px solid var(--teal);
    background:linear-gradient(160deg,#e9e5e2,#b89a88)}
  .bubble{position:absolute;left:42px;top:143px;width:235px;height:76px;background:var(--white);border-radius:8px;
    box-shadow:0 2px 6px rgba(0,0,0,.08);display:flex;align-items:center;justify-content:center;text-align:center;
    font-family:'Arvo',serif;font-size:14px;line-height:20px;letter-spacing:.5px;padding:0 38px}
  .bubble-tail{position:absolute;left:150px;top:218px;width:30px;height:24px}
  .swipe{position:absolute;top:172px;width:10px;height:16px}
  .swipe--prev{left:13px}
  .swipe--next{left:295px}
  .bubble-go{left:284px;top:143px}
  .tip-card{position:absolute;left:42px;top:267px;width:235px;height:178px;background:var(--white);border-radius:8px;
    box-shadow:0 2px 6px rgba(0,0,0,.08);padding:11px 12px;text-align:center;font-family:'Arvo',serif;font-size:11px;line-height:19.8px}
  .ad-banner{position:absolute;left:12px;top:474px;width:293px;height:36px;background:var(--ad);overflow:hidden;
    border:1px solid #c96a1c;display:flex;align-items:center}
  .ad-art{position:absolute;left:12px;top:-2px;width:50px;height:50px;border-radius:50%;background:linear-gradient(#ffffff,#e6e6e6);border:2px solid #333}
  .ad-copy{position:absolute;left:80px;width:140px;text-align:center;color:var(--white);font-size:8.5px;font-weight:700;line-height:11px}
  .ad-brand{position:absolute;right:8px;color:var(--white);font-size:15px;font-weight:700}
</style>
</head>
<body>
<main class="board">

  <section class="screen screen--welcome">
    <svg class="header-curve" viewBox="0 0 318 160" aria-hidden="true">
      <path d="M0 0H318V84C240 150 78 150 0 84Z" fill="var(--teal)"/>
      <path d="M0 0H318V72C240 140 78 140 0 72Z" fill="var(--ink)"/>
    </svg>
    <div class="hero-photo" role="img" aria-label="Photo of a smiling couple cheek to cheek"></div>
    <h1 class="app-title">ROMANCE<br>PROMPT ACE</h1>
    <p class="app-subtitle">ROMANCE PROMPT ACE</p>
    <div class="pill pill--dark">GET STARTED
      <svg class="go-icon" viewBox="0 0 22 22" aria-hidden="true"><circle cx="11" cy="11" r="11" fill="var(--green)"/><path d="M9 6l5 5-5 5" stroke="var(--ink)" stroke-width="3" fill="none" stroke-linecap="round" stroke-linejoin="round"/></svg>
    </div>
    <span class="page-count">X10</span>
  </section>

  <section class="screen screen--menu">
    <svg class="header-curve" viewBox="0 0 318 160" aria-hidden="true">
      <path d="M0 0H318V54C250 104 68 130 0 72Z" fill="var(--teal)"/>
      <path d="M0 0H318V56C250 116 68 116 0 56Z" fill="var(--ink)"/>
    </svg>
    <div class="nav-back"><svg viewBox="0 0 7 10"><path d="M6 1L2 5l4 4" stroke="#fff" stroke-width="2" fill="none"/></svg>BACK</div>
    <div class="nav-place"><div class="city">San Francisco</div><div class="stamp">26 July 6:26 AM</div></div>
    <div class="avatar" style="left:12px" role="img" aria-label="Portrait of a man with glasses"></div>
    <div class="avatar" style="left:79px" role="img" aria-label="Portrait of a dark-haired woman"></div>
    <div class="avatar" style="left:181px" role="img" aria-label="Portrait of a young man"></div>
    <div class="avatar" style="left:248px" role="img" aria-label="Portrait of a blonde woman"></div>
    <div class="pill pill--dark">DATING QUESTIONS
      <svg class="go-icon" viewBox="0 0 22 22" aria-hidden="true"><circle cx="11" cy="11" r="11" fill="var(--green)"/><path d="M9 6l5 5-5 5" stroke="var(--ink)" stroke-width="3" fill="none" stroke-linecap="round" stroke-linejoin="round"/></svg>
    </div>
    <div class="pill pill--teal">DATING TIPS</div>
    <span class="page-count">X10</span>
  </section>

  <section class="screen screen--tip">
    <svg class="header-curve" viewBox="0 0 318 160" aria-hidden="true">
      <path d="M0 0H318V54C250 104 68 130 0 72Z" fill="var(--teal)"/>
      <path d="M0 0H318V56C250 116 68 116 0 56Z" fill="var(--ink)"/>
    </svg>
    <div class="nav-back"><svg viewBox="0 0 7 10"><path d="M6 1L2 5l4 4" stroke="#fff" stroke-width="2" fill="none"/></svg>BACK</div>
    <div class="nav-place"><div class="city">San Francisco</div><div class="stamp">26 July 6:26 AM</div></div>
    <svg class="swipe swipe--prev" viewBox="0 0 10 16" aria-hidden="true"><path d="M8 2L3 8l5 6" stroke="var(--ink)" stroke-width="2.5" fill="none"/></svg>
    <div class="bubble">Keep the conversation equal</div>
    <svg class="bubble-tail" viewBox="0 0 30 24" aria-hidden="true"><path d="M0 0H28L25 24Z" fill="var(--white)"/></svg>
    <svg class="go-icon bubble-go" viewBox="0 0 22 22" aria-hidden="true"><circle cx="11" cy="11" r="11" fill="var(--green)"/><path d="M9 6l5 5-5 5" stroke="var(--white)" stroke-width="3" fill="none" stroke-linecap="round" stroke-linejoin="round"/></svg>
    <svg class="swipe swipe--next" viewBox="0 0 10 16" aria-hidden="true"><path d="M2 2l5 6-5 6" stroke="var(--ink)" stroke-width="2.5" fill="none"/></svg>
    <div class="tip-card">A great conversation is one where both parties feel engaged and are equally contributing. When your date shares something about themselves or asks you a question, always reply by sharing a similar story or asking them the same question.</div>
    <aside class="ad-banner">
      <div class="ad-art" role="img" aria-label="Cartoon illustration for the advert"></div>
      <div class="ad-copy">Find your next home to rent<br>in just a few taps</div>
      <div class="ad-brand">letbay</div>
    </aside>
    <span class="page-count">X10</span>
  </section>

  <section class="screen screen--question">
    <svg class="header-curve" viewBox="0 0 318 160" aria-hidden="true">
      <path d="M0 0H318V54C250 104 68 130 0 72Z" fill="var(--teal)"/>
      <path d="M0 0H318V56C250 116 68 116 0 56Z" fill="var(--ink)"/>
    </svg>
    <div class="nav-back"><svg viewBox="0 0 7 10"><path d="M6 1L2 5l4 4" stroke="#fff" stroke-width="2" fill="none"/></svg>BACK</div>
    <div class="nav-place"><div class="city">San Francisco</div><div class="stamp">26 July 6:26 AM</div></div>
    <svg class="swipe swipe--prev" viewBox="0 0 10 16" aria-hidden="true"><path d="M8 2L3 8l5 6" stroke="var(--ink)" stroke-width="2.5" fill="none"/></svg>
    <div class="bubble">What makes you laugh?</div>
    <svg class="bubble-tail" viewBox="0 0 30 24" aria-hidden="true"><path d="M0 0H28L25 24Z" fill="var(--white)"/></svg>
    <svg class="go-icon bubble-go" viewBox="0 0 22 22" aria-hidden="true"><circle cx="11" cy="11" r="11" fill="var(--green)"/><path d="M9 6l5 5-5 5" stroke="var(--white)" stroke-width="3" fill="none" stroke-linecap="round" stroke-linejoin="round"/></svg>
    <svg class="swipe swipe--next" viewBox="0 0 10 16" aria-hidden="true"><path d="M2 2l5 6-5 6" stroke="var(--ink)" stroke-width="2.5" fill="none"/></svg>
    <aside class="ad-banner">
      <div class="ad-art" role="img" aria-label="Cartoon illustration for the advert"></div>
      <div class="ad-copy">Find your next home to rent<br>in just a few taps</div>
      <div class="ad-brand">letbay</div>
    </aside>
    <span class="page-count">X10</span>
  </section>

</main>
</body>
</html>
```